Meridale Eating needs Stationary and a business card

We would like to use our current logo. The text can be moved around as needed. The stationary needs to be a 'first page' where the logo is more prominent to be impressive on higher quality paper and a second page where the logo is more subtle where there will be much more information on the page. There are 2 clinic locations which will need include name, address, phone number, fax number, web address. The business card should be single sided and contain this information also.
The design must be contemporary and sophisticated as this is a science based diet run out of a medical clinic.

Target Market(s)

People wanting to lose weight, athletes looking to optimise performance, people with arthritis or fighting cancer

Industry/Entity Type

Business

Contact Information for Business Card

must use the logo. I have attached an example card with the practice details on it. there must be space for the doctors name. Also the website www.meridaleeating.example.au

Requirements
Must have
• the logo, the business adresses and phone numbers, the website, the doctors name and qualifications
Nice to have
• some creativity
Should not have
• Do not simply reproduce the existing card please

```html
<!DOCTYPE html>
<html lang="en">
<head>
<meta charset="utf-8">
<title>Meridale Eating – Stationery</title>
<link href="https://fonts.googleapis.com/css2?family=Jost:wght@400;500;600&display=swap" rel="stylesheet">
<style>
  :root{
    --backdrop:#cfcfcf;
    --paper:#ffffff;
    --card:#f7f7f7;
    --brand-dark:#1f5fa8;
    --brand-light:#35ace6;
    --ink:#222222;
    --muted:#555555;
  }
  *{box-sizing:border-box;margin:0;padding:0}
  html,body{width:1200px;height:1200px;overflow:hidden}
  body{background:var(--backdrop);font-family:"Jost",sans-serif;color:var(--ink);position:relative}

  .letterhead{position:absolute;left:305px;top:136px;width:666px;height:944px;background:var(--paper)}
  .brand{position:absolute;display:flex;flex-direction:column;align-items:center}
  .brand-dot{border-radius:50%;background:var(--brand-light)}
  .brand-name{font-weight:600;color:var(--brand-dark);white-space:nowrap;letter-spacing:-0.2px}

  .letterhead .brand{left:233px;top:28px;width:200px}
  .letterhead .brand-dot{width:80px;height:80px}
  .letterhead .brand-name{font-size:19px;margin-top:10px}

  .watermark{position:absolute;left:179px;top:304px;width:336px;height:336px;border-radius:50%;
    background:radial-gradient(circle,#e8f2f9 0%,#e3edf4 70%,#dde6ee 100%);opacity:.85}

  .clinics{display:grid;font-weight:400;white-space:nowrap}
  .clinic{padding:0 6px}
  .clinic--left{text-align:right;border-right:1px solid var(--brand-light)}
  .clinic-name{color:var(--brand-light);font-weight:500}
  .clinic-gap{display:block}

  .letterhead-footer{position:absolute;left:5px;right:35px;top:828px;display:flex;align-items:flex-end}
  .letterhead .clinics{grid-template-columns:160px auto;font-size:11px;line-height:1.3}
  .letterhead .clinic{padding:0 7px}
  .letterhead .clinic-gap{height:8px}
  .footer-rule{flex:1;height:1.5px;margin:0 0 3px 10px;background:var(--brand-light)}

  .doctor{position:absolute;text-align:right}
  .doctor-name{font-weight:600;color:var(--ink)}
  .doctor-quals{color:var(--muted)}
  .doctor-role{color:var(--brand-light);font-weight:500}
  .letterhead .doctor{right:38px;top:850px}
  .letterhead .doctor-name{font-size:15px}
  .letterhead .doctor-quals{font-size:5px;letter-spacing:.1px}
  .letterhead .doctor-role{font-size:8.5px}

  .card{position:absolute;width:290px;height:178px;background:var(--card)}
  .card--details{left:198px;top:521px;background:#fbfbfb}
  .card--brand{left:198px;top:744px}
  .card--details .brand{left:10px;top:20px;width:110px}
  .card--details .brand-dot{width:62px;height:62px}
  .card--details .brand-name{font-size:10.5px;margin-top:8px}
  .card--brand .brand{left:60px;top:44px;width:170px}
  .card--brand .brand-dot{width:64px;height:64px}
  .card--brand .brand-name{font-size:11px;margin-top:9px}

  .card .doctor{left:140px;top:47px;width:100px;text-align:center}
  .card .doctor-name{font-size:8px}
  .card .doctor-quals{font-size:3px}
  .card .doctor-role{font-size:6.5px}
  .card .clinics{position:absolute;left:96px;top:106px;grid-template-columns:95px auto;font-size:6.6px;line-height:1.38}
  .card .clinic{padding:0 5px}
  .card .clinic-gap{height:6px}
</style>
</head>
<body>
  <section class="letterhead">
    <div class="brand">
      <span class="brand-dot"></span>
      <span class="brand-name">MERIDALE EATING</span>
    </div>
    <div class="watermark" role="img" aria-label="Faint enlarged brand emblem placed as a background decoration"></div>

    <div class="doctor">
      <div class="doctor-name">Dr Elian Marsh</div>
      <div class="doctor-quals">MBBS (NSW) MBiomedE FRACS (Ortho) FAOrthA</div>
      <div class="doctor-role">Orthopaedic Surgeon</div>
    </div>

    <footer class="letterhead-footer">
      <div class="clinics">
        <div class="clinic clinic--left">
          <span class="clinic-name">Westmere</span><br>Knee Surgery
          <span class="clinic-gap"></span>
          Tel: 02 9100 4821<br>www.westknee.example.au<br>212 Halden Road<br>Westmere NSW 2090
        </div>
        <div class="clinic">
          <span class="clinic-name">Ashgrove</span><br>Shoulder and Elbow
          <span class="clinic-gap"></span>
          Tel: 02 9100 7362<br>www.emarsh.example.au<br>58-60 Carrow Road<br>Ashgrove NSW 2145
        </div>
      </div>
      <div class="footer-rule"></div>
    </footer>
  </section>

  <section class="card card--details">
    <div class="brand">
      <span class="brand-dot"></span>
      <span class="brand-name">MERIDALE EATING</span>
    </div>
    <div class="doctor">
      <div class="doctor-name">Dr Elian Marsh</div>
      <div class="doctor-quals">MBBS (NSW) MBiomedE FRACS (Ortho) FAOrthA</div>
      <div class="doctor-role">Orthopaedic Surgeon</div>
    </div>
    <div class="clinics">
      <div class="clinic clinic--left">
        <span class="clinic-name">Westmere</span><br>Knee Surgery
        <span class="clinic-gap"></span>
        212 Halden Road<br>Westmere NSW 2090<br>02 9100 4821<br>www.westknee.example.au
      </div>
      <div class="clinic">
        <span class="clinic-name">Ashgrove</span><br>Shoulder and Elbow
        <span class="clinic-gap"></span>
        58-60 Carrow Road<br>Ashgrove NSW 2145<br>02 9100 7362<br>www.emarsh.example.au
      </div>
    </div>
  </section>

  <section class="card card--brand">
    <div class="brand">
      <span class="brand-dot"></span>
      <span class="brand-name">MERIDALE EATING</span>
    </div>
  </section>
</body>
</html>
```